Company Profile for Consulting Comany

Need Company profile to be designed in a professional way.

for inspiring :-
https://www.vimolia.net/gallery/5307462/COMPANY-PROFILE
https://www.vimolia.net/gallery/20934617/Biotech-Product-Catalog-No1-(Laminar-Air-Flow)
https://www.vimolia.net/gallery/38720954/RKT-Tramvale-Company-Profile-2014-(RKT-Rebrand-part-2)

Target Market(s)

Corporate

Industry/Entity Type

It Company

Font styles to use
Sans Serif

Requirements
Must have
• Landscape A4 size
• Must go with the logo branding
• Must Have Visual Identity is the most important
• Must Have mpty spaces

```html
<!DOCTYPE html>
<html lang="en">
<head>
<meta charset="utf-8">
<title>Shiftwell Advisory — Company Profile</title>
<link rel="stylesheet" href="https://fonts.googleapis.com/css2?family=Open+Sans:wght@300;400;600;700&display=swap">
<style>
:root{
  --cyan:#2bb5d8;
  --cyan-dark:#1e95b5;
  --ink:#1c1e21;
  --ink-2:#2a2d31;
  --band:#3a3d42;
  --grey:#6b6e72;
  --line:#c9ccd0;
  --paper:#ffffff;
  --canvas:#e9eaec;
  --light:#f3f4f5;
}
*{box-sizing:border-box;margin:0;padding:0}
html,body{width:1200px;height:2473px;overflow:hidden;background:var(--canvas);font-family:"Open Sans",Arial,sans-serif;color:var(--grey)}
.canvas{position:relative;width:1200px;height:2473px}
.page{position:absolute;overflow:hidden;background:var(--paper)}
.page.dark{background:var(--ink)}
.abs{position:absolute}
.photo{position:absolute}
.logo{position:absolute;display:flex;align-items:center;gap:6px}
.logo .mark{width:22px;height:22px;background:var(--cyan)}
.logo .name{font-weight:700;color:var(--cyan);font-size:15px;line-height:1;letter-spacing:.2px}
.tagline{position:absolute;font-size:7px;color:var(--cyan)}
.page-no{position:absolute;top:12px;right:18px;font-size:7px;color:var(--grey);letter-spacing:.5px}
.h-title{position:absolute;font-weight:300;color:var(--cyan);font-size:22px;letter-spacing:.5px}
.band{position:absolute;left:18px;right:18px;height:30px;background:var(--band);border-bottom:2px solid var(--cyan)}
.band .label{position:absolute;left:12px;top:9px;font-size:10px;color:var(--cyan);letter-spacing:.4px}
.band .logo{right:10px;top:5px}
.band .logo .mark{width:16px;height:16px}
.band .logo .name{font-size:10px}
.p{font-size:6.5px;line-height:1.45;color:var(--grey)}
.p.w{color:#e8eaec}
.sub{font-size:7px;font-weight:600;color:var(--cyan);letter-spacing:.3px;margin-bottom:2px;text-transform:uppercase}
.frame{position:absolute;border:1px solid rgba(255,255,255,.28)}
.frame.dim{border-color:rgba(0,0,0,.09)}

/* cover */
.cover .hero-band{position:absolute;left:0;top:194px;width:412px;height:94px;background:var(--cyan)}
.cover .hero-band .kicker{position:absolute;left:22px;top:16px;font-size:13px;color:#0d3a47;letter-spacing:.5px}
.cover .hero-band .headline{position:absolute;left:22px;top:38px;font-size:31px;font-weight:300;color:#fff;letter-spacing:.5px}
.cover .pillars{position:absolute;left:22px;bottom:12px;font-size:10px;color:#d8dadd;letter-spacing:1.5px}

/* toc */
.toc{position:absolute;left:22px;right:30px;top:95px;list-style:none}
.toc li{display:flex;justify-content:space-between;font-size:7px;line-height:10.6px;color:var(--grey);border-bottom:1px dotted #e1e3e5}

/* who */
.exec{position:absolute;left:0;top:100px;width:193px;height:272px;background:var(--ink);padding:26px 14px 0 14px}
.exec .sub{color:#fff}
.mission{position:absolute;left:193px;top:100px;width:335px;height:272px;background:var(--cyan);padding:10px 14px}
.mission .sub{color:#fff}
.mission ul{list-style:none}
.values{width:100%;border-collapse:collapse;margin-top:4px}
.values td{font-size:6.5px;color:#fff;padding:4px 0;border-bottom:1px solid rgba(255,255,255,.35);vertical-align:top}
.values td:first-child{width:115px;text-transform:uppercase}

/* why */
.why-item{position:absolute;width:240px;display:flex;gap:8px}
.why-item .thumb{flex:0 0 80px;height:58px}
.why-item .sub{font-size:6.5px}

/* what */
.train{position:absolute;left:0;bottom:0;width:100%;height:118px;background:var(--ink);padding:10px 16px}
.train .sub{margin-top:4px}
.svc{position:absolute;list-style:none}
.svc li{font-size:6.5px;line-height:12px;color:var(--grey)}
.svc li::before{content:"";display:inline-block;width:4px;height:4px;background:var(--cyan);margin-right:5px;vertical-align:middle}

/* talent */
.icons{position:absolute;left:18px;right:18px;top:200px;height:150px;background:var(--cyan);display:grid;grid-template-columns:repeat(3,1fr);grid-template-rows:1fr 1fr}
.icons .cell{display:flex;flex-direction:column;align-items:center;justify-content:center;gap:6px;border-right:1px solid rgba(255,255,255,.3);border-bottom:1px solid rgba(255,255,255,.3)}
.icons .cell span{font-size:6.5px;color:#fff;letter-spacing:.3px}

/* partners */
.partner{position:absolute;left:18px;display:flex;align-items:center;gap:5px;font-size:14px;font-weight:600;color:var(--band)}
.partner i{display:block;width:10px;height:10px;background:var(--cyan)}
.partner-text{position:absolute;left:160px;right:18px;top:56px}
.partner-text .block{margin-bottom:8px}

/* team */
.member{position:absolute;left:16px;right:18px;display:flex;gap:10px}
.member .face{flex:0 0 48px;height:56px}

/* certifications */
.badge{position:absolute}
.section-rule{position:absolute;left:18px;right:18px;height:1px;background:var(--line)}
.section-title{position:absolute;left:18px;font-size:8px;color:var(--band);letter-spacing:.5px}
.contact{position:absolute;left:14px;top:218px;width:175px}
.contact .p{font-size:6px}
</style>
</head>
<body>
<div class="canvas">

  <!-- Cover -->
  <section class="page dark cover" style="left:59px;top:41px;width:528px;height:363px">
    <div class="photo" role="img" aria-label="Night view of glass office towers in a city skyline" style="inset:0;background:linear-gradient(135deg,#15171a 0%,#262a2f 55%,#3a3f45 100%)"></div>
    <div class="logo" style="left:22px;top:40px">
      <div class="mark" style="width:34px;height:34px"></div>
      <div class="name" style="font-size:21px">Shiftwell Advisory</div>
    </div>
    <div class="tagline" style="left:62px;top:72px;font-size:8px">A Step Toward Change</div>
    <div class="hero-band">
      <div class="kicker">WE CAN HELP YOU TO</div>
      <div class="headline">MAKE CHANGE HAPPEN</div>
    </div>
    <div class="frame" style="left:380px;top:280px;width:140px;height:60px"></div>
    <div class="frame" style="left:410px;top:300px;width:90px;height:38px"></div>
    <div class="frame" style="left:120px;top:310px;width:230px;height:40px;border-color:rgba(255,255,255,.12)"></div>
    <div class="pillars">STRATEGY | PEOPLE | TECHNOLOGY</div>
  </section>

  <!-- Spread: inside cover + contents -->
  <section class="page dark" style="left:59px;top:442px;width:528px;height:372px">
    <div class="frame" style="left:250px;top:110px;width:300px;height:190px;border-color:rgba(255,255,255,.18)"></div>
    <div class="frame" style="left:300px;top:160px;width:230px;height:130px;border-color:rgba(255,255,255,.14)"></div>
    <div class="frame" style="left:100px;top:200px;width:210px;height:120px;border-color:rgba(255,255,255,.1)"></div>
    <div class="frame" style="left:380px;top:260px;width:110px;height:80px;border-color:rgba(255,255,255,.2)"></div>
  </section>
  <section class="page" style="left:587px;top:442px;width:554px;height:372px">
    <div class="band" style="top:18px;background:#44484d"><div class="label" style="color:#fff">TABLE OF CONTENTS</div>
      <div class="logo"><div class="mark"></div><div class="name">Shiftwell Advisory</div></div></div>
    <ul class="toc">
      <li><span>Who we are?</span><span>2</span></li>
      <li><span>Executive Summary</span><span>2</span></li>
      <li><span>Vision</span><span>2</span></li>
      <li><span>Mission</span><span>2</span></li>
      <li><span>Values</span><span>2</span></li>
      <li><span>Why Shiftwell Advisory?</span><span>3</span></li>
      <li><span>What we do?</span><span>4</span></li>
      <li><span>HR &amp; OD Consultation</span><span>4</span></li>
      <li><span>Professional Training</span><span>4</span></li>
      <li><span>Talent Assessment</span><span>5</span></li>
      <li><span>HR Solutions</span><span>5</span></li>
      <li><span>Partnership</span><span>6</span></li>
      <li><span>Norvane Implementation Partners</span><span>6</span></li>
      <li><span>Brightwater Group</span><span>6</span></li>
      <li><span>Talora</span><span>6</span></li>
      <li><span>Corvessa Consulting</span><span>6</span></li>
      <li><span>Our Team</span><span>7</span></li>
      <li><span>Karim Haddad / Consulting Manager</span><span>7</span></li>
      <li><span>Tarek Nasser / Senior Consultant</span><span>7</span></li>
      <li><span>Faisal Al Murr / Projects Manager</span><span>7</span></li>
      <li><span>Lina Saeed / Associate Consultant</span><span>7</span></li>
      <li><span>Certifications</span><span>8</span></li>
      <li><span>Our Clients</span><span>8</span></li>
      <li><span>Contact us</span><span>8</span></li>
    </ul>
    <div class="logo" style="right:20px;bottom:14px"><div class="mark" style="width:18px;height:18px"></div><div class="name" style="font-size:11px">Shiftwell Advisory</div></div>
  </section>

  <!-- Spread: who we are / why -->
  <section class="page" style="left:59px;top:844px;width:528px;height:372px">
    <div class="page-no">PAGE 2</div>
    <div class="h-title" style="left:20px;top:38px">WHO WE ARE?</div>
    <div class="exec">
      <div class="sub">Executive Summary</div>
      <p class="p w">Shiftwell Advisory is a professional HR &amp; OD organization specialized in talent and organizational development, career coaching, leadership assessment and development, total reward, HR technology and payroll services. We combine regional knowledge with global expertise to help organizations across the Middle East grow, adapt and perform through people-driven change programs and trusted partnerships.</p>
      <div class="sub" style="margin-top:10px">Vision</div>
      <p class="p w">"To become the leading HR partner in the Middle East and stand known for quality services."</p>
    </div>
    <div class="mission">
      <div class="sub">Mission</div>
      <p class="p w">We are a multi-layered mission driven to meet the needs of our customers by increasing the value of our services and upgrading our standing among our competitors.</p>
      <ul class="p w" style="margin-top:3px">
        <li>- To provide convenient HR solutions to SMEs as they focus on their core business.</li>
        <li>- To play our role in economic development of the region.</li>
        <li>- To develop a professional relationship with our valued clients and investors.</li>
        <li>- To bring innovation in HR services through technology.</li>
      </ul>
      <div class="sub" style="margin-top:8px">Values</div>
      <table class="values">
        <tr><td>Integrity</td><td>We act with integrity, honesty and respect in every client relationship.</td></tr>
        <tr><td>Workplace Empowerment</td><td>We empower every team member to grow and to lead with confidence.</td></tr>
        <tr><td>Accountability</td><td>We own our results and stay accountable for our actions and choices.</td></tr>
        <tr><td>Pursuit of Excellence</td><td>We bring the highest standards to each project and every service.</td></tr>
        <tr><td>Quality Control</td><td>We review and refine our work to deliver dependable outcomes.</td></tr>
        <tr><td>Affordability</td><td>We keep our services affordable to meet the needs of all clients.</td></tr>
      </table>
    </div>
  </section>
  <section class="page" style="left:587px;top:844px;width:554px;height:372px">
    <div class="page-no">PAGE 3</div>
    <div class="band" style="top:26px"><div class="label">WHY SHIFTWELL ADVISORY?</div>
      <div class="logo"><div class="mark"></div><div class="name">Shiftwell Advisory</div></div></div>
    <div class="frame dim" style="left:30px;top:80px;width:500px;height:270px"></div>
    <div class="frame dim" style="left:200px;top:140px;width:330px;height:220px"></div>
    <div class="why-item" style="left:36px;top:84px">
      <div class="thumb photo" role="img" aria-label="Business people shaking hands" style="position:relative;background:linear-gradient(135deg,#b9c7d2,#6f8595)"></div>
      <div><div class="sub">Success</div><p class="p">We will deliver tailored results for you. We will ensure that our people are of the highest calibre, with real experience in your field.</p></div>
    </div>
    <div class="why-item" style="left:290px;top:84px">
      <div class="thumb photo" role="img" aria-label="Confident business professional in a suit" style="position:relative;background:linear-gradient(135deg,#d4d9de,#7d8790)"></div>
      <div><div class="sub">Superior Workforce</div><p class="p">Our dedicated training professionals have all been rigorously screened, selected and trained to give you expert support.</p></div>
    </div>
    <div class="why-item" style="left:36px;top:172px">
      <div class="thumb photo" role="img" aria-label="Hands reviewing charts on a desk" style="position:relative;background:linear-gradient(135deg,#dfe4e8,#8fa0ac)"></div>
      <div><div class="sub">Targeting</div><p class="p">We understand the importance of targeting the right people and connecting them to the right roles at the right time.</p></div>
    </div>
    <div class="why-item" style="left:290px;top:172px">
      <div class="thumb photo" role="img" aria-label="Team working together at a laptop" style="position:relative;background:linear-gradient(135deg,#c9d3da,#6d7f8c)"></div>
      <div><div class="sub">Flexible Multichannel Abilities</div><p class="p">We take capabilities into account across all channels, so we can adapt to your changing needs.</p></div>
    </div>
    <div class="why-item" style="left:290px;top:256px">
      <div style="flex:0 0 80px"></div>
      <div><div class="sub">Cost Effectiveness</div><p class="p">Change starts with solutions that are affordable, offering real value and lasting returns for every project.</p></div>
    </div>
  </section>

  <!-- Spread: what we do / talent assessment -->
  <section class="page" style="left:59px;top:1244px;width:528px;height:372px">
    <div class="photo" role="img" aria-label="Hands signing business documents on a desk" style="left:0;top:0;width:528px;height:150px;background:linear-gradient(120deg,#2c3a45 0%,#56697a 55%,#9aa8b3 100%)"></div>
    <div class="logo" style="left:14px;top:12px"><div class="mark"></div><div class="name" style="font-size:12px">Shiftwell Advisory</div></div>
    <div class="page-no" style="color:#e2e5e8">PAGE 4</div>
    <div class="h-title" style="left:16px;top:98px;font-size:26px">WHAT WE DO?</div>
    <div class="abs" style="left:16px;top:160px;width:175px">
      <div class="sub">HR &amp; OD Consultation</div>
      <p class="p">Our dedicated team of HR and OD experts is on hand to provide professional support for all your HR and OD operations and development. Working closely alongside your organization, we will identify gaps in your current situation and propose solutions to overcome them.</p>
    </div>
    <ul class="svc" style="left:205px;top:160px">
      <li>HR Strategic Alignment</li>
      <li>Organizational Design &amp; Development</li>
      <li>Talent Assessment &amp; Management</li>
      <li>Learning &amp; Leadership Development</li>
      <li>Communication &amp; Change Management</li>
    </ul>
    <ul class="svc" style="left:365px;top:160px">
      <li>Compensation &amp; Benefits</li>
      <li>Work-life Initiatives</li>
      <li>Performance &amp; Recognition</li>
      <li>Development &amp; Career Opportunities</li>
      <li>Coaching &amp; Mentoring Program</li>
    </ul>
    <div class="train">
      <div class="sub">Professional Training</div>
      <p class="p w">Our vocational training services enable people and organizations to optimize the skills, knowledge and abilities of their workforce. We deliver a broad range of training courses, including qualifications and customized sessions.</p>
      <div class="sub">In House Custom Training</div>
      <p class="p w">We are committed to provide a high quality training that adds value to our client's employees and their business processes, built on proven methods.</p>
      <div class="sub">Professional Qualifications</div>
      <p class="p w">We are proud to introduce a portfolio of recognized qualifications that are valued globally for their benefit to knowledge, skills and competencies.</p>
    </div>
  </section>
  <section class="page" style="left:587px;top:1244px;width:554px;height:372px">
    <div class="abs" style="left:18px;top:10px;font-size:8px;color:var(--band);letter-spacing:.4px">TALENT ASSESSMENT</div>
    <div class="section-rule" style="top:24px"></div>
    <div class="page-no">PAGE 5</div>
    <p class="p abs" style="left:18px;top:34px;width:145px">Our carefully developed assessment solutions allow you to assess the skills, aptitudes and abilities of your workforce, enabling you to identify and fill any skills gaps.</p>
    <div class="abs" style="left:180px;top:34px;width:355px">
      <div class="sub">Talent Assessment</div>
      <p class="p">Assessing people for best performance is the most important task of any organization. The quality of assessment ultimately determines the performance of new hires as well as the ability of the organization to deliver on its promises.</p>
      <div class="sub" style="margin-top:6px">Talent Management</div>
      <p class="p">As an organization strives to meet its business goals, it must make sure that it has a continuous and integrated process for recruiting, onboarding, developing and retaining people. We can help you identify and implement the best approach.</p>
    </div>
    <div class="abs" style="left:18px;top:140px;width:518px">
      <div class="sub">HR Solutions</div>
      <p class="p">Outsourcing: a trusted HRMS solution combined with regional expertise now brings your HR administration and payroll outsourcing to one place. Whether you are a corporate client with special payroll requirements or a small enterprise seeking confidentiality and accuracy, we have proven ourselves to be a reliable business partner.</p>
    </div>
    <div class="icons">
      <div class="cell"><svg width="26" height="20" viewBox="0 0 26 20" fill="#fff"><circle cx="8" cy="5" r="4"/><circle cx="18" cy="5" r="4"/><path d="M0 20c0-6 4-8 8-8s8 2 8 8zM12 20c1-5 3-8 6-8 4 0 8 2 8 8z"/></svg><span>EMPLOYEE RELATIONS</span></div>
      <div class="cell"><svg width="26" height="20" viewBox="0 0 26 20" fill="none" stroke="#fff" stroke-width="2"><rect x="1" y="3" width="24" height="15" rx="2"/><path d="M1 8h24"/></svg><span>PAYROLL AND PAY</span></div>
      <div class="cell" style="border-right:none"><svg width="26" height="20" viewBox="0 0 26 20" fill="#fff"><rect x="1" y="12" width="5" height="8"/><rect x="9" y="8" width="5" height="12"/><rect x="17" y="3" width="5" height="17"/></svg><span>WORK INCREASE PROCESSING</span></div>
      <div class="cell" style="border-bottom:none"><svg width="20" height="20" viewBox="0 0 20 20" fill="none" stroke="#fff" stroke-width="2"><path d="M3 18L17 2"/><circle cx="5" cy="5" r="3"/><circle cx="15" cy="15" r="3"/></svg><span>INCENTIVES &amp; BONUS</span></div>
      <div class="cell" style="border-bottom:none"><svg width="22" height="20" viewBox="0 0 22 20" fill="none" stroke="#fff" stroke-width="2"><rect x="1" y="3" width="14" height="16"/><path d="M9 13l10-10 2 2-10 10H9z" fill="#fff"/></svg><span>RECRUITMENT &amp; HIRING</span></div>
      <div class="cell" style="border:none"><svg width="22" height="22" viewBox="0 0 22 22" fill="#fff"><path d="M10 2a9 9 0 1 0 9 9h-9z"/><path d="M12 0v9h9a9 9 0 0 0-9-9z"/></svg><span>PERFORMANCE MANAGEMENT</span></div>
    </div>
  </section>

  <!-- Spread: partners / team -->
  <section class="page" style="left:59px;top:1641px;width:528px;height:372px">
    <div class="page-no">PAGE 6</div>
    <div class="band" style="top:22px"><div class="label" style="color:#fff">SUCCESS PARTNERSHIP</div>
      <div class="logo"><div class="mark"></div><div class="name">Shiftwell Advisory</div></div></div>
    <div class="partner" style="top:66px"><i></i>Norvane</div>
    <div class="partner" style="top:112px"><i></i>Keldra</div>
    <div class="partner" style="top:158px"><i></i>Brightwater</div>
    <div class="partner" style="top:208px"><i></i>Tidepoint</div>
    <div class="partner" style="top:254px"><i></i>Talora</div>
    <div class="partner" style="top:300px"><i></i>Corvessa</div>
    <div class="partner-text">
      <div class="block"><div class="sub">Norvane Implementation Partners</div><p class="p">Norvane is an international consulting firm that guides organizations through all types of complex change. Its methodology has been applied extensively in leading companies around the world.</p></div>
      <div class="block"><div class="sub">Brightwater Group</div><p class="p">Brightwater Group is a distance learning center that offers qualification units and accredited courses. Their programs are developed for HR professionals across many industries.</p></div>
      <div class="block"><div class="sub">Tidepoint</div><p class="p">With over 20 years of experience working closely with HR directors and managers, Tidepoint can help your organization achieve its goals by developing strategies that build engaged teams.</p></div>
      <div class="block"><div class="sub">Talora</div><p class="p">Talora HCM is a comprehensive human capital management system that streamlines your HR processes, from recruitment and attendance to payroll and employee self service.</p></div>
      <div class="block"><div class="sub">Corvessa Consulting</div><p class="p">Corvessa is an organization specialized in providing customized leadership development solutions to companies in the region, recognizing the value of local insight.</p></div>
    </div>
  </section>
  <section class="page" style="left:587px;top:1641px;width:554px;height:372px">
    <div class="photo" role="img" aria-label="Business team meeting around a table" style="left:0;top:0;width:554px;height:106px;background:linear-gradient(120deg,#3b4650 0%,#6a7a87 60%,#a9b4bc 100%)"></div>
    <div class="page-no" style="color:#e2e5e8">PAGE 7</div>
    <div class="h-title" style="left:14px;top:44px;font-size:32px">OUR TEAM</div>
    <div class="member" style="top:118px">
      <div class="face photo" role="img" aria-label="Portrait of the consulting manager" style="position:relative;background:linear-gradient(180deg,#b7bec4,#5f6870)"></div>
      <div><div class="sub">Karim Haddad - Consulting Manager</div><p class="p">Certified HR practitioner with more than 15 years of exceptional local and international business track record in talent and OD, combined across several industries including banking, construction, retail, pharmaceutical and manufacturing. Experienced in computer programming, business administration and HR practices.</p></div>
    </div>
    <div class="member" style="top:202px">
      <div class="face photo" role="img" aria-label="Portrait of the senior consultant" style="position:relative;background:linear-gradient(180deg,#b7bec4,#5f6870)"></div>
      <div><div class="sub">Tarek Nasser - Senior Consultant</div><p class="p">Certified HR practitioner with more than 12 years of experience working in Saudi Arabia and the Gulf region, holding qualifications in coaching, change management and OD. His areas of strength are engaging teams in profound change interventions through coaching and facilitated learning.</p></div>
    </div>
    <div class="member" style="top:286px">
      <div class="face photo" role="img" aria-label="Portrait of the projects manager" style="position:relative;background:linear-gradient(180deg,#b7bec4,#5f6870)"></div>
      <div><div class="sub">Faisal Al Murr - Projects Manager</div><p class="p">Certified systems professional and project manager with more than ten years of experience and in-depth understanding of HR project implementations. He has delivered major integrations and training projects for several large enterprises in the Kingdom.</p></div>
    </div>
  </section>

  <!-- Spread: certifications & clients / back cover -->
  <section class="page" style="left:59px;top:2044px;width:528px;height:372px">
    <div class="section-title" style="top:12px">CERTIFICATIONS</div>
    <div class="page-no">PAGE 8</div>
    <div class="section-rule" style="top:26px"></div>
    <div class="badge" style="left:18px;top:40px;width:108px;height:20px;background:#1f3f7a"></div>
    <div class="badge" style="left:140px;top:40px;width:92px;height:20px;background:#2f5b97"></div>
    <div class="badge" style="left:246px;top:38px;width:80px;height:22px;background:#3b3f44"></div>
    <div class="badge" style="left:338px;top:36px;width:44px;height:58px;background:#111"></div>
    <div class="badge" style="left:392px;top:40px;width:70px;height:22px;background:#5b3d8f"></div>
    <div class="badge" style="left:468px;top:38px;width:42px;height:24px;background:#6b2a7a"></div>
    <div class="badge" style="left:18px;top:72px;width:108px;height:20px;background:#2d4f8f"></div>
    <div class="badge" style="left:140px;top:74px;width:54px;height:16px;background:#2a6fb5"></div>
    <div class="badge" style="left:206px;top:72px;width:62px;height:20px;background:#3a6aa6"></div>
    <div class="badge" style="left:392px;top:72px;width:80px;height:20px;background:#5b6068"></div>
    <div class="badge" style="left:18px;top:104px;width:88px;height:20px;background:#1e3a6b"></div>
    <div class="section-title" style="top:208px">OUR CLIENTS</div>
    <div class="section-rule" style="top:222px"></div>
    <div class="badge" style="left:22px;top:260px;width:56px;height:36px;background:#3a8a4e;border-radius:50%"></div>
    <div class="badge" style="left:92px;top:262px;width:60px;height:30px;background:#2b77b8"></div>
    <div class="badge" style="left:166px;top:262px;width:74px;height:30px;background:#24426e"></div>
    <div class="badge" style="left:258px;top:262px;width:70px;height:30px;background:#3f7fa8"></div>
    <div class="badge" style="left:340px;top:264px;width:40px;height:28px;background:#ef7d1a"></div>
    <div class="badge" style="left:392px;top:262px;width:72px;height:30px;background:#3d7ac0"></div>
    <div class="badge" style="left:22px;top:310px;width:68px;height:30px;background:#1f5ea8"></div>
  </section>
  <section class="page" style="left:587px;top:2044px;width:554px;height:372px">
    <div class="contact">
      <div class="sub" style="font-size:9px;font-weight:400;margin-bottom:6px">CONTACT US</div>
      <p class="p" style="font-weight:600;color:var(--band)">DUBAI</p>
      <p class="p">PO Box 40218, Dubai, UAE<br>21st Floor, Harbor Plaza, Tower 2, Marina Road<br>T: +971 4 555 0142<br>F: +971 4 555 0143<br>E: info@shiftwelladvisory.example</p>
      <p class="p" style="font-weight:600;color:var(--band);margin-top:6px">KHOBAR</p>
      <p class="p">PO Box 77305, Khobar, Saudi Arabia<br>2nd Floor, Palm Gate Tower, Coastal Road<br>T: +966 13 555 0187<br>E: info@shiftwelladvisory.example</p>
    </div>
    <div class="photo" role="img" aria-label="Dark blurred office interior backdrop" style="left:195px;top:0;width:359px;height:372px;background:radial-gradient(ellipse at 50% 45%,#3c4f60 0%,#253340 55%,#18212a 100%)"></div>
    <div class="logo" style="left:258px;top:160px">
      <div class="mark" style="width:40px;height:40px"></div>
      <div class="name" style="font-size:22px">Shiftwell Advisory</div>
    </div>
    <div class="tagline" style="left:305px;top:204px;font-size:9px">A Step Toward Change</div>
  </section>

</div>
</body>
</html>
```